Velra Orchards Business Cards

design business cards for our new business should match my Copperline Quotes business cards

Contact Information for Business Card

2817 N 48th W Ave
Brenton, OK 74210

Requirements
Must have
• should match logo colors

```html
<!DOCTYPE html>
<html lang="en">
<head>
<meta charset="UTF-8">
<title>Velra Orchards Business Cards</title>
<link rel="stylesheet" href="https://fonts.googleapis.com/css2?family=Michroma&family=Open+Sans:wght@400;600&display=swap">
<style>
  :root {
    --canvas: #e4e5e8;
    --card-dark: #03111a;
    --card-teal: #083742;
    --leaf-green: #7cc83c;
    --aqua: #1fc0c9;
    --white: #ffffff;
    --rule: #3e7d3a;
  }
  * { box-sizing: border-box; margin: 0; padding: 0; }
  html, body {
    width: 1200px; height: 800px; overflow: hidden;
    background: var(--canvas);
  }
  .stage {
    width: 1200px; height: 800px;
    display: flex; align-items: center; justify-content: center; gap: 40px;
  }
  .card {
    position: relative;
    width: 540px; height: 309px;
    background: linear-gradient(135deg, var(--card-dark) 0%, var(--card-teal) 100%);
    box-shadow: 0 10px 28px rgba(0,0,0,.18);
    overflow: hidden;
  }
  .wordmark {
    font-family: "Michroma", sans-serif;
    font-weight: 400;
    color: var(--leaf-green);
    line-height: 1.1;
    text-transform: uppercase;
    white-space: nowrap;
  }
  .wordmark .primary { display: block; font-size: 46px; letter-spacing: 4px; }
  .wordmark .secondary { display: block; font-size: 20px; letter-spacing: 11px; margin-top: 8px; }
  .card-front .wordmark {
    position: absolute; left: 50%; top: 50%;
    transform: translate(-50%, -50%);
    text-align: center;
  }
  .card-back .wordmark {
    position: absolute; left: 38px; top: 100px;
  }
  .card-back .wordmark .primary { font-size: 36px; letter-spacing: 3px; }
  .card-back .wordmark .secondary { font-size: 15px; letter-spacing: 8px; }
  .divider {
    position: absolute; left: 310px; top: 78px;
    width: 1px; height: 122px;
    background: var(--rule);
  }
  .address {
    position: absolute; left: 332px; top: 116px;
    font-family: "Open Sans", sans-serif;
    font-style: normal;
    font-size: 14px; line-height: 1.45;
    display: flex; gap: 8px; align-items: flex-start;
    white-space: nowrap;
  }
  .address .icon { margin-top: 3px; flex: none; }
  .address .street { color: var(--leaf-green); display: block; }
  .address .city { color: var(--aqua); display: block; }
  .corner-bands { position: absolute; left: 0; bottom: 0; }
</style>
</head>
<body>
<main class="stage">
  <section class="card card-front" aria-label="Card front">
    <div class="wordmark">
      <span class="primary">Velra</span>
      <span class="secondary">Orchards</span>
    </div>
  </section>

  <section class="card card-back" aria-label="Card back">
    <div class="wordmark">
      <span class="primary">Velra</span>
      <span class="secondary">Orchards</span>
    </div>
    <div class="divider"></div>
    <address class="address">
      <svg class="icon" width="14" height="13" viewBox="0 0 14 13" aria-hidden="true">
        <path d="M7 0 L14 6 H12 V13 H8.5 V9 H5.5 V13 H2 V6 H0 Z" fill="#ffffff"/>
      </svg>
      <span>
        <span class="street">2817 N 48th W Ave</span>
        <span class="city">Brenton, OK 74210</span>
      </span>
    </address>
    <svg class="corner-bands" width="540" height="309" viewBox="0 0 540 309" aria-hidden="true">
      <defs>
        <linearGradient id="band-fade" x1="0" y1="0" x2="1" y2="0">
          <stop offset="0" stop-color="#7cc83c"/>
          <stop offset="0.6" stop-color="#7cc83c"/>
          <stop offset="1" stop-color="#1fc0c9"/>
        </linearGradient>
      </defs>
      <polygon points="266,309 278,309 262,288 250,288" fill="#ffffff"/>
      <polygon points="286,309 540,309 540,288 270,288" fill="url(#band-fade)"/>
    </svg>
  </section>
</main>
</body>
</html>
```